EPIC, awesome, creative business card needed - get involved!

I'm launching a boutique, exclusive Property Management real estate agency in Sydney early next year.
The name of the agency will be called "Silver Oak Lane" - it's a play on "follow the yellow brick road" to wealth. The Silver Oak Lane signifies wealth through property investment.
My business will offer management of investment properties (ie Property Management).
The difference with Silver Oak Lane and other agencies is the business will be run by one of Australia's leading property investment experts, and also one of Australia's leading property managers.
It will be exclusively for high net worth properties and individuals, so the business card needs to be extremely sharp, slick and relatively simple.
The information I want on the card is as follows
Marcus Fenwick - Director
M: 0471 926 154
P: 9637 0518
E: marcus@silveroaklane.net.au
W: silveroaklane.net.au
I'm happy with the red from the logo, black - no yellows or funky colors. I want this to be a super corporate and slick business card to match the high end nature of the business.
Good luck everyone, and please ask questions for clarification.

```html
<!DOCTYPE html>
<html lang="en">
<head>
<meta charset="utf-8">
<title>Silver Oak Lane – Business Card</title>
<link rel="stylesheet" href="https://fonts.googleapis.com/css2?family=Roboto+Condensed:wght@400;700&display=swap">
<style>
  :root {
    --brand-red: #b3121b;
    --ink: #111111;
    --card-black: #000000;
    --paper: #ffffff;
    --canvas: #ffffff;
    --edge: #d6d6d6;
  }
  * { margin: 0; padding: 0; box-sizing: border-box; }
  html, body {
    width: 1200px; height: 2400px; overflow: hidden;
    background: var(--canvas);
    font-family: "Roboto Condensed", "Arial Narrow", sans-serif;
  }
  .canvas { position: relative; width: 1200px; height: 2400px; }

  /* Front */
  .card-front {
    position: absolute; left: 96px; top: 200px;
    width: 1008px; height: 568px;
    background: var(--card-black);
    border-radius: 40px;
  }
  .front-brand {
    position: absolute; left: 0; right: 0; top: 150px;
    text-align: center;
    color: var(--brand-red);
    font-weight: 700; font-size: 62px; line-height: 0.95;
    text-transform: uppercase; letter-spacing: 1px;
  }
  .front-web {
    position: absolute; left: 0; right: 0; top: 404px;
    text-align: center;
    color: var(--brand-red);
    font-weight: 700; font-size: 34px;
  }

  /* Back */
  .card-back {
    position: absolute; left: 88px; top: 932px;
    width: 1024px; height: 560px;
    background: var(--paper);
    border: 3px solid var(--edge);
    border-radius: 40px;
    overflow: hidden;
  }
  .band-rule {
    position: absolute; left: 0; right: 0; height: 3px;
    background: var(--brand-red);
  }
  .band-rule.top { top: 216px; }
  .band-rule.bottom { top: 345px; }
  .back-brand {
    position: absolute; left: 0; top: 216px;
    width: 196px; height: 132px;
    background: var(--brand-red);
    display: flex; flex-direction: column; justify-content: center;
    padding-left: 40px;
    color: var(--paper);
    font-weight: 700; font-size: 26px; line-height: 0.98;
    text-transform: uppercase;
  }
  .contact-list {
    position: absolute; left: 222px; top: 222px;
    list-style: none;
  }
  .contact-list li {
    display: flex; align-items: center;
    height: 40px;
    font-size: 29px; color: var(--ink);
  }
  .contact-list li::before {
    content: ""; width: 18px; height: 18px;
    background: var(--brand-red);
    margin-right: 22px;
  }
  .name-plate {
    position: absolute; right: 0; top: 216px;
    width: 384px; height: 132px;
    background: var(--brand-red);
    color: var(--paper);
    display: flex; flex-direction: column; align-items: center; justify-content: center;
  }
  .person-name { font-weight: 700; font-size: 54px; line-height: 1; }
  .person-role { font-weight: 400; font-size: 26px; margin-top: 4px; }
</style>
</head>
<body>
<main class="canvas">
  <section class="card-front" aria-label="Card front">
    <div class="front-brand">Silver<br>Oak<br>Lane</div>
    <div class="front-web">silveroaklane.net.au</div>
  </section>

  <section class="card-back" aria-label="Card back">
    <div class="band-rule top"></div>
    <div class="band-rule bottom"></div>
    <div class="back-brand">Silver<br>Oak<br>Lane</div>
    <ul class="contact-list">
      <li>M: 0471 926 154</li>
      <li>P: 9637 0518</li>
      <li>E: marcus@silveroaklane.net.au</li>
    </ul>
    <div class="name-plate">
      <span class="person-name">Marcus Fenwick</span>
      <span class="person-role">Director</span>
    </div>
  </section>
</main>
</body>
</html>
```